Label Design for 2x Chutney Products

We need a label design for 2x Chutney Products.
Zintara Chutney - Red Chili
Zintara Chutney - Green Chili & Coriander
See attached pictures. This is just sample pictures so you get an impression of the product and the colors. Both labels to have as title the generic name "Zintara Chutney" and then added either Red Chili or Green Chili & Coriander. The different terms needs to be good readable and can differ in font/color/size, or in the same style if this makes more sense from design point (as I am not a designer). The labels later on need to be editable in the way that the ingredient list, nutrition list, basis company and production information can be added. If this needs to be done directly and cannot be edited later on please let know. Editable design related the additional text also would be good as the additional information need to be added in different languages (Dutch. German and perhaps French). No clue how this is to be implemented but looking forward to receive some input/solutions on this.
I already had a project to create the company logo. I consider this logo to be used as the product logo and not the company logo. A different company logo later on can be designed from new. This logo is here attached. Either to work with this logo and use it as product logo (perhaps revise the colors) and add the product description or create a new logo for the product from scratch if you feel too. The logo itself should be easily readable for the product name/description and the colors appealing to such product and of course customers.
Please contact if any clarification needed. Thanks in advance for your efforts and ideas for this project.

Industry/Entity Type

Food

Other font styles liked:
• Asian Touch

Requirements
Nice to have
• If possible "simply" editable for text fields in order to add/revise the ingredient list, nutrition list, revise to different languages.

```html
<!DOCTYPE html>
<html lang="en">
<head>
<meta charset="utf-8">
<title>Zintara Chutney – Green Chili &amp; Coriander label</title>
<link href="https://fonts.googleapis.com/css2?family=Arimo:wght@400&family=Montserrat:wght@300;500;700&display=swap" rel="stylesheet">
<style>
  :root {
    --label-black: #000000;
    --text-white: #ffffff;
    --leaf-green: #7cc242;
    --leaf-deep: #2f5a17;
    --chili-red: #d8312a;
  }
  * { margin: 0; padding: 0; box-sizing: border-box; }
  html, body { width: 1200px; height: 296px; overflow: hidden; background: var(--label-black); }
  .label {
    position: relative;
    width: 1200px;
    height: 296px;
    background: var(--label-black);
    color: var(--text-white);
    font-family: "Arimo", Arial, sans-serif;
    overflow: hidden;
  }
  .coriander-art {
    position: absolute;
    left: 460px;
    top: 0;
    width: 740px;
    height: 296px;
    background:
      radial-gradient(ellipse 220px 130px at 260px 60px, rgba(124,194,66,0.55), rgba(124,194,66,0) 70%),
      radial-gradient(ellipse 200px 160px at 640px 230px, rgba(124,194,66,0.45), rgba(124,194,66,0) 70%),
      radial-gradient(ellipse 160px 110px at 520px 130px, rgba(47,90,23,0.6), rgba(47,90,23,0) 70%);
  }
  .chili-art {
    position: absolute;
    left: 280px;
    top: 110px;
    width: 135px;
    height: 186px;
    background: radial-gradient(ellipse 55px 90px at 60px 100px, rgba(124,194,66,0.5), rgba(124,194,66,0) 75%);
  }
  .info-column {
    position: absolute;
    top: 26px;
    width: 300px;
    font-size: 16px;
    line-height: 20px;
  }
  .info-column p + p { margin-top: 20px; }
  .info-left { left: 20px; }
  .info-right { left: 892px; }
  .brand-mark {
    position: absolute;
    left: 288px;
    top: 14px;
    width: 110px;
    text-align: center;
    font-family: "Montserrat", sans-serif;
    font-weight: 700;
    font-size: 15px;
    line-height: 17px;
    color: var(--leaf-green);
  }
  .brand-dot {
    display: block;
    width: 48px;
    height: 48px;
    margin: 0 auto 8px;
    border-radius: 50%;
    background: var(--chili-red);
  }
  .product-title {
    position: absolute;
    left: 410px;
    top: 140px;
    font-family: "Montserrat", sans-serif;
  }
  .title-brand {
    display: block;
    font-weight: 300;
    font-size: 40px;
    line-height: 44px;
    letter-spacing: 3px;
  }
  .title-product {
    display: block;
    font-weight: 700;
    font-size: 62px;
    line-height: 62px;
    letter-spacing: 2px;
  }
  .title-variant {
    display: block;
    margin-top: 8px;
    font-weight: 500;
    font-size: 22px;
    letter-spacing: 1.5px;
    color: var(--leaf-green);
  }
</style>
</head>
<body>
  <main class="label">
    <div class="coriander-art" role="img" aria-label="Line illustration of fresh coriander leaves in green"></div>
    <div class="chili-art" role="img" aria-label="Line illustration of green chili peppers"></div>

    <section class="info-column info-left">
      <p>Lorem ipsum dolor sit amet,<br>consectetuer adipiscing elit,<br>sed diam nonummy nibh<br>euismod</p>
      <p>tincidunt ut laoreet dolore<br>magna aliquam erat volutpat.<br>Ut wisi enim ad minim veniam,<br>quis nostrud exerci tation</p>
      <p>Ut wisi enim ad minim veniam,<br>quis nostrud exerci tation</p>
    </section>

    <div class="brand-mark"><span class="brand-dot"></span>KELVRA<br>FOODS</div>

    <h1 class="product-title">
      <span class="title-brand">ZINTARA</span>
      <span class="title-product">CHUTNEY</span>
      <span class="title-variant">Green Chili &amp; Coriander</span>
    </h1>

    <section class="info-column info-right">
      <p>Lorem ipsum dolor sit amet,<br>consectetuer adipiscing elit,<br>sed diam nonummy nibh<br>euismod</p>
      <p>tincidunt ut laoreet dolore<br>magna aliquam erat volutpat.<br>Ut wisi enim ad minim veniam,<br>quis nostrud exerci tation</p>
      <p>Ut wisi enim ad minim veniam,<br>quis nostrud exerci tation</p>
    </section>
  </main>
</body>
</html>
```